Weekly Newsletter

Each week I send out a news update to the entire company updating everyone on the news and accomplishments of the week. I've been sending in an email but would like to start sending in a template that looks more professional. Either still in an email or perhaps something that can be turned into a PDF.
Each week I try to include something from each department:

• Headquarters
• MD Service
• Construction
• NOVA
• Richmond
• Hampton Roads
• Rockville
• Forestville
• Fleet
• Safety
• HR

For more info www.TrevalonPowerworks.com

Target Market(s)

Employees within the company. Might include an announcement area.

Industry/Entity Type

Electrical Power

Font styles to use
Sans Serif

Requirements
Must have
• Logo and style. awesome graphics

```html
<!DOCTYPE html>
<html lang="en">
<head>
<meta charset="utf-8">
<title>Trevalon Powerworks Weekly Newsletter</title>
<link href="https://fonts.googleapis.com/css2?family=Hind:wght@400;500;600;700&display=swap" rel="stylesheet">
<style>
:root{
  --red:#e8101c;
  --red-dark:#c70d17;
  --navy:#1f2a7a;
  --ink:#222;
  --body:#555;
  --header-bg:#f5f5f5;
  --section-bg:#ededf0;
  --line:#d3d3d6;
  --white:#fff;
}
*{box-sizing:border-box;margin:0;padding:0}
html,body{width:1200px;height:2184px;overflow:hidden}
body{font-family:"Hind",Arial,sans-serif;background:var(--white);color:var(--ink);position:relative}
.site-header{height:145px;background:var(--header-bg);position:relative}
.contact{position:absolute;top:60px;display:flex;align-items:center;gap:8px;font-size:15px;color:var(--ink)}
.contact--email{left:120px}
.contact--phone{left:956px}
.brand{position:absolute;left:0;right:0;top:34px;text-align:center;color:var(--red);font-weight:700;line-height:1}
.brand__name{font-size:30px;letter-spacing:1px;display:block}
.brand__tag{font-size:13px;letter-spacing:1px;display:block;margin-top:4px}
.hero{position:absolute;top:145px;left:0;width:1200px;height:666px;background:linear-gradient(180deg,#8f9297 0%,#6d6f70 40%,#5b5b55 62%,#7d7a72 100%)}
.hero__title{position:absolute;top:330px;left:0;right:0;text-align:center;color:var(--white);font-size:35px;font-weight:600}
.btn{position:absolute;left:480px;top:394px;width:222px;height:42px;border-radius:21px;background:var(--red);color:var(--white);font-size:14px;font-weight:600;display:flex;align-items:center;justify-content:center;letter-spacing:.3px}
.news{position:absolute;top:811px;left:0;width:1200px;height:654px;background:var(--section-bg)}
.dept-nav{position:absolute;left:103px;top:79px;width:233px;border:1px solid var(--line);background:var(--section-bg);list-style:none}
.dept-nav li{height:44.3px;border-top:1px solid var(--line);padding-left:16px;display:flex;align-items:center;font-size:16px;color:#444}
.dept-nav li:first-child{border-top:none;font-size:18px;font-weight:600;color:var(--ink)}
.dept-nav li.is-active{background:var(--red);color:var(--white)}
.report{position:absolute;left:386px;top:79px;width:714px}
.report__photo{height:228px;background:linear-gradient(180deg,#5d6066 0%,#d9d9d6 55%,#8a5a3c 100%)}
.report__title{font-size:23px;font-weight:600;margin-top:10px;color:var(--ink)}
.report__body{margin-top:22px;padding:0 3px;font-size:15px;line-height:17.5px;color:var(--body);text-align:justify}
.report__body p+p{margin-top:17px}
.gallery__item{position:absolute}
.site-footer{position:absolute;top:2083px;left:0;width:1200px;height:101px;background:var(--red);color:var(--white)}
.site-footer__copy{position:absolute;left:84px;top:40px;font-size:15px;font-weight:600}
.social{position:absolute;right:80px;top:37px;display:flex;gap:12px;list-style:none}
.social li{width:26px;height:26px;border-radius:50%;background:var(--white)}
</style>
</head>
<body>
<header class="site-header">
  <div class="contact contact--email">
    <svg width="24" height="24" viewBox="0 0 24 24"><circle cx="12" cy="12" r="11" fill="none" stroke="#e8101c" stroke-width="2"/><rect x="6.5" y="8" width="11" height="8" fill="none" stroke="#e8101c" stroke-width="1.6"/><path d="M6.5 8l5.5 4.5L17.5 8" fill="none" stroke="#e8101c" stroke-width="1.6"/></svg>
    <span>info@trevalonpowerworks.com</span>
  </div>
  <div class="brand">
    <span class="brand__name">TREVALON POWERWORKS</span>
    <span class="brand__tag">INCORPORATED</span>
  </div>
  <div class="contact contact--phone">
    <svg width="24" height="24" viewBox="0 0 24 24"><circle cx="12" cy="12" r="11" fill="none" stroke="#e8101c" stroke-width="2"/><path d="M8.5 7c-1 1-1 3 1 6s4.5 4.5 6 4l1-1.5-2.2-1.6-1.2 1c-1.2-.6-2.6-2-3.2-3.2l1-1.2L9.3 6.3z" fill="none" stroke="#e8101c" stroke-width="1.5" stroke-linejoin="round"/></svg>
    <span>877.555.0142</span>
  </div>
</header>

<section class="hero" role="img" aria-label="Photo of a lineman in a bucket truck servicing a street lamp beside a fenced bridge">
  <h1 class="hero__title">Trusted and reliable lighting experts</h1>
  <span class="btn">READ MORE</span>
</section>

<section class="news">
  <ul class="dept-nav">
    <li>Headquarters</li>
    <li>MD Service</li>
    <li>Construction</li>
    <li>NOVA</li>
    <li>Richmond</li>
    <li>Hampton Roads</li>
    <li class="is-active">Rockville</li>
    <li>Forestville</li>
    <li>Fleet</li>
    <li>Safety</li>
    <li>HR</li>
  </ul>
  <article class="report">
    <div class="report__photo" role="img" aria-label="Photo of a warehouse interior lit by new high-bay fixtures"></div>
    <h2 class="report__title">Rockville:</h2>
    <div class="report__body">
      <p>This week Marco Estevan and Luis Adano continued work on the Ashgrove Rd. construction project installing Voltera splice boxes, conduit, fiberglass poles, and Colonial post top fixtures. With the nice weather forecasted next week this project will be completed. They both also proceeded to set and picked up several knockdowns throughout Montgomery County.</p>
      <p>&bull;&nbsp;&nbsp;&nbsp;&nbsp;Dale Whitford and Ron Palmer resumed progress group re-lamping in the Gaithersburg and Olney areas. They both additionally completed all of Montgomery County's 311 calls, took care of all expedited outage calls provided by county residents, as well as installing multiple fixtures.</p>
      <p>Great week gentlemen, thank you!</p>
    </div>
  </article>
</section>

<section class="gallery">
  <div class="gallery__item" style="left:0;top:1465px;width:601px;height:301px;background:linear-gradient(135deg,#6b7a95,#2c3f82)" role="img" aria-label="Photo of an employee holding an award plaque in front of a company photo wall"></div>
  <div class="gallery__item" style="left:610px;top:1465px;width:305px;height:301px;background:linear-gradient(160deg,#4f6b3a,#2a3424)" role="img" aria-label="Photo of a technician in hi-vis vest repairing a traffic signal"></div>
  <div class="gallery__item" style="left:923px;top:1465px;width:277px;height:301px;background:linear-gradient(180deg,#0e0f12,#2b3033)" role="img" aria-label="Night photo of a crew and trucks under a bright pole light"></div>
  <div class="gallery__item" style="left:0;top:1775px;width:287px;height:300px;background:linear-gradient(180deg,#8c8f94,#4d4a48)" role="img" aria-label="Photo of a crew working on a street light from a truck"></div>
  <div class="gallery__item" style="left:296px;top:1775px;width:305px;height:300px;background:linear-gradient(135deg,#5a5552,#1e1e1e)" role="img" aria-label="Photo of an employee holding an award plaque"></div>
  <div class="gallery__item" style="left:610px;top:1775px;width:590px;height:300px;background:linear-gradient(160deg,#6f8a55,#3f5a2c)" role="img" aria-label="Photo of a walkway with railing and a utility cabinet on the lawn"></div>
</section>

<footer class="site-footer">
  <p class="site-footer__copy">Copyright &copy; 2018 Trevalon Powerworks. All Rights Reserved.</p>
  <ul class="social">
    <li></li><li></li><li></li><li></li><li></li>
  </ul>
</footer>
</body>
</html>
```